Medical Company in need of Modern business card design for new Wound Care clinic.

Modern business card design for our Woundcare company. Logo and description of services can be found on our website; https://www.tovrel-woundcare.com/

```html
<!DOCTYPE html>
<html lang="en">
<head>
<meta charset="utf-8">
<title>Tovrel Woundcare – Business Card</title>
<link rel="stylesheet" href="https://fonts.googleapis.com/css2?family=Montserrat:wght@400;500;600&display=swap">
<style>
  :root {
    --stage: #3a3b3e;
    --card-dark: #1b1b1b;
    --card-light: #ffffff;
    --gold: #c18f2e;
    --gold-light: #e6bd62;
    --ink: #3c3c3c;
    --rule: #b5b5b5;
    --pattern-a: #232323;
    --pattern-b: #1d1d1d;
  }
  * { box-sizing: border-box; margin: 0; padding: 0; }
  html, body { width: 1200px; height: 895px; overflow: hidden; }
  body {
    background: var(--stage);
    font-family: "Montserrat", sans-serif;
    position: relative;
  }
  .card {
    position: absolute;
    top: 132px;
    width: 360px;
    height: 630px;
    border-radius: 18px;
    overflow: hidden;
  }
  /* Back of card */
  .card-back { left: 190px; background: var(--card-dark); }
  .back-pattern {
    position: absolute;
    top: 0; right: 0;
    width: 100%; height: 62%;
    background: linear-gradient(200deg, var(--pattern-a) 0%, var(--pattern-b) 70%, var(--card-dark) 100%);
  }
  .back-brand {
    position: absolute;
    left: 0; right: 0; bottom: 110px;
    display: flex; flex-direction: column; align-items: center; gap: 22px;
  }
  .brand-mark {
    width: 46px; height: 46px;
    background: var(--gold);
  }
  .back-name {
    color: var(--gold);
    font-weight: 500;
    font-size: 22px;
    letter-spacing: 4px;
  }
  /* Front of card */
  .card-front { left: 650px; background: var(--card-light); }
  .front-brand {
    position: absolute;
    top: 58px; left: 0; right: 0;
    display: flex; flex-direction: column; align-items: center; gap: 16px;
  }
  .front-brand .brand-mark { width: 70px; height: 70px; border-radius: 50%; }
  .front-brand-name {
    color: var(--gold);
    font-weight: 500;
    font-size: 19px;
    letter-spacing: 3px;
  }
  .front-body {
    position: absolute;
    top: 250px; left: 44px; right: 44px;
  }
  .person-name {
    color: var(--gold);
    font-weight: 500;
    font-size: 25px;
    letter-spacing: 0.5px;
  }
  .person-title {
    color: var(--ink);
    font-size: 15px;
    margin-top: 4px;
  }
  .icon-row {
    display: flex; align-items: center; gap: 6px;
    margin: 26px 0 22px;
  }
  .icon-row .rule { flex: 1; height: 1px; background: var(--rule); }
  .icon {
    width: 26px; height: 26px;
    border-radius: 50%;
    background: linear-gradient(135deg, var(--gold-light), var(--gold));
    display: flex; align-items: center; justify-content: center;
  }
  .contact-list { list-style: none; color: var(--ink); font-size: 15.5px; line-height: 1.5; }
  .divider { height: 1px; background: var(--rule); margin: 24px 0 20px; }
  .address { font-style: normal; color: var(--ink); font-size: 15.5px; line-height: 1.5; }
</style>
</head>
<body>

<section class="card card-back">
  <div class="back-pattern" role="img" aria-label="Repeating faint brand-mark pattern"></div>
  <div class="back-brand">
    <span class="brand-mark"></span>
    <span class="back-name">TOVREL WOUNDCARE</span>
  </div>
</section>

<section class="card card-front">
  <div class="front-brand">
    <span class="brand-mark"></span>
    <span class="front-brand-name">TOVREL WOUNDCARE</span>
  </div>

  <div class="front-body">
    <h1 class="person-name">RAFAEL DUNMORE</h1>
    <p class="person-title">Expert-comptable diplômé</p>

    <div class="icon-row">
      <span class="rule"></span>
      <span class="icon">
        <svg width="14" height="14" viewBox="0 0 24 24" fill="#fff"><path d="M6.6 10.8a15 15 0 0 0 6.6 6.6l2.2-2.2a1 1 0 0 1 1-.25 11.4 11.4 0 0 0 3.6.57 1 1 0 0 1 1 1V20a1 1 0 0 1-1 1A17 17 0 0 1 3 4a1 1 0 0 1 1-1h3.5a1 1 0 0 1 1 1c0 1.25.2 2.45.57 3.57a1 1 0 0 1-.25 1z"/></svg>
      </span>
      <span class="icon">
        <svg width="14" height="14" viewBox="0 0 24 24" fill="none" stroke="#fff" stroke-width="2"><rect x="3" y="6" width="18" height="12" rx="1"/><path d="M3 7l9 6 9-6"/></svg>
      </span>
      <span class="icon">
        <svg width="14" height="14" viewBox="0 0 24 24" fill="none" stroke="#fff" stroke-width="1.8"><circle cx="12" cy="12" r="9"/><path d="M3 12h18M12 3c3 3 3 15 0 18M12 3c-3 3-3 15 0 18"/></svg>
      </span>
      <span class="rule"></span>
    </div>

    <ul class="contact-list">
      <li>972-555-0147</li>
      <li>rd@tovrel-woundcare.com</li>
      <li>tovrel-woundcare.com</li>
    </ul>

    <div class="divider"></div>

    <address class="address">
      2180 Harlow Ave Ste 200 PMB<br>
      412076 Dallas, TX 75219
    </address>
  </div>
</section>

</body>
</html>
```